Touring Cabaret Seasons Needs a Poster Design

We need a poster design for upcoming Cabaret seasons in Melbourne and Adelaide (Australia) for a prestigious festival.

Show is titled "Here's a Small Thing I Dreamed Up Last Week..." and is a comedy parody of bad cabaret and deluded performers. We'd like the poster to reflect the comedy of the piece without being silly and inaccessable.

Artist has recently won awards for this show and these will need to be listed as a part of the design.

I have attached a couple of photographs that can be used - one is the artist with a blank book cover and these could be used to overlay text.

Would like it to not look too wordy, however I realise we've asked for a lot of text to be included.

Target Market(s)

Ages 20 - 40 cabaret or comedy fans.

Industry/Entity Type

Festival

Requirements
Must have
• TEXT:
The Velvet Parlour presents:
Here's a Small Thing I Dreamed Up Last Week...

TEXT:
WINNER of BEST CABARET, BEST WRITING and PEOPLE’S CHOICE awards at Quick + Tidy Revue 2011

TEXT:
The Lantern Room (Melbourne)
Feb 23rd to the 26th

Le Corbeau, REVedge(Adelaide)
March 3rd and 4th

QUOTES:
“...the funniest things in spandex. 4.5 stars” – The Courier Post on Rally! A revue about lawn bowls.

“a clever dissection of bad cabaret” – Owen Blackwood, The Courier Post on Quick + Tidy Revue
Nice to have
• TEXT:
The last time someone showed you a little something they were working on, did you lose an hour of your life you will never get back? Don’t worry – we’ve all been there.

TEXT:
Composer and co-writer of Rally! (A revue about lawn bowls) and WINNER of BEST CABARET, BEST WRITING and PEOPLE’S CHOICE awards at Quick + Tidy Revue 2011, presents her full show, with more original music and helpful anecdotes.

WEBSITE:
More info at www.mingleface.example/thevelvetparlour

```html
<!DOCTYPE html>
<html lang="en">
<head>
<meta charset="utf-8">
<title>Here's a Small Thing I Dreamed Up Last Week... — The Velvet Parlour</title>
<link rel="stylesheet" href="https://fonts.googleapis.com/css2?family=Mulish:ital,wght@0,400;0,600;0,700;0,800;1,400&display=swap">
<style>
  :root {
    --ink: #000000;
    --paper: #ffffff;
    --peach: #f6c58c;
    --muted: #d8d8d8;
    --stage-glow: #3a2a22;
    --stage-floor: #6a3418;
    --laurel: #2a2a2a;
  }
  * { margin: 0; padding: 0; box-sizing: border-box; }
  html, body { width: 848px; height: 1200px; overflow: hidden; background: var(--ink); }
  body { font-family: "Mulish", sans-serif; color: var(--paper); }
  .poster { position: relative; width: 848px; height: 1200px; overflow: hidden; background: var(--ink); }

  .stage-photo {
    position: absolute; left: 440px; top: 470px; width: 408px; height: 730px;
    background:
      radial-gradient(ellipse 55% 30% at 45% 88%, var(--stage-floor) 0%, rgba(60,25,10,0.6) 45%, transparent 80%),
      radial-gradient(ellipse 40% 50% at 45% 45%, var(--stage-glow) 0%, rgba(20,14,12,0.6) 50%, transparent 85%);
  }

  .teaser {
    position: absolute; top: 82px; left: 0; width: 848px; text-align: center;
    font-style: italic; font-size: 19px; line-height: 32px;
  }
  .teaser strong { font-style: normal; font-weight: 700; display: block; }

  .billing { position: absolute; right: 474px; top: 352px; text-align: right; }
  .company { font-weight: 700; font-size: 17px; line-height: 20px; }
  .presents { font-weight: 700; font-size: 13px; line-height: 16px; }

  .title {
    position: absolute; right: 474px; top: 412px; text-align: right;
    color: var(--peach); font-weight: 700; font-size: 46px; line-height: 48px; letter-spacing: -0.5px;
  }

  .seasons { position: absolute; right: 474px; top: 694px; text-align: right; font-size: 14px; line-height: 21px; }
  .season { margin-bottom: 28px; }
  .venue { font-weight: 700; }

  .quote { position: absolute; right: 370px; text-align: right; }
  .quote blockquote { font-weight: 700; font-size: 25px; line-height: 25px; }
  .quote cite { display: block; font-style: normal; font-size: 10px; margin-top: 8px; color: var(--muted); }
  .quote-one { top: 862px; }
  .quote-two { top: 964px; right: 366px; }

  .website { position: absolute; left: 99px; top: 1036px; font-size: 14px; }

  .award { position: absolute; left: 505px; top: 330px; width: 210px; height: 160px; }
  .laurel { position: absolute; top: 10px; width: 36px; height: 130px; background: var(--laurel); border-radius: 50%; }
  .laurel-left { left: 0; }
  .laurel-right { right: 0; }
  .award-text { position: absolute; left: 36px; right: 36px; top: 28px; text-align: center; }
  .award-note { font-weight: 800; font-size: 9px; line-height: 11px; text-transform: uppercase; }
  .award-name { font-weight: 800; font-size: 20px; line-height: 20px; text-transform: uppercase; margin-top: 10px; }
  .award-year { font-weight: 700; font-size: 14px; margin-top: 24px; }
</style>
</head>
<body>
<main class="poster">
  <div class="stage-photo" role="img" aria-label="Performer in a long black gown and gold gloves posing under a stage spotlight"></div>

  <p class="teaser">
    The last time someone showed<br>
    you a little something they were working on,<br>
    did you lose a year of your life you will never get back?
    <strong>Don’t worry – we’ve all been there.</strong>
  </p>

  <div class="billing">
    <p class="company">The Velvet Parlour</p>
    <p class="presents">presents:</p>
  </div>

  <h1 class="title">Here's<br>a Small<br>Thing I<br>Dreamed Up<br>Last Week...</h1>

  <section class="award" aria-label="Award">
    <div class="laurel laurel-left" role="img" aria-label="Laurel branch"></div>
    <div class="laurel laurel-right" role="img" aria-label="Laurel branch"></div>
    <div class="award-text">
      <p class="award-note">Winner<br>Best Cabaret, Best Writing<br>&amp; People’s Choice Awards</p>
      <p class="award-name">Quick + Tidy<br>Revue</p>
      <p class="award-year">2011</p>
    </div>
  </section>

  <section class="seasons">
    <div class="season">
      <p class="venue">The Lantern Room (Melbourne)</p>
      <p>Feb 23rd to the 26th</p>
    </div>
    <div class="season">
      <p class="venue">Le Corbeau, REVedge (Adelaide)</p>
      <p>March 3rd and 4th</p>
    </div>
  </section>

  <figure class="quote quote-one">
    <blockquote>“...the funniest things<br>in spandex. 4.5 stars”</blockquote>
    <cite>– The Courier Post on Rally! A revue about lawn bowls.</cite>
  </figure>

  <figure class="quote quote-two">
    <blockquote>“a clever dissection<br>of bad cabaret”</blockquote>
    <cite>– Owen Blackwood, The Courier Post on Quick + Tidy Revue</cite>
  </figure>

  <p class="website">www.mingleface.example/thevelvetparlour</p>
</main>
</body>
</html>
```